Business card design for IT consulting company

Looking for a simple, modern, clean business card design.
Open to reworking our existing logo.

Attached is our current business cards which we do not like.
Ideally double sided with something simple on the back.
Rectangle / Horizonal only.
No rounded edges on the card.
White as the dominate color is preferred.

Target Market(s)

clients, legal, oil & gas, medical, professionals

Industry/Entity Type

IT, tech, consulting

Contact Information for Business Card

Name, Title, email, phone, cell, website

Font styles to use
Sans Serif

Requirements
Must have
• Clean design
Should not have
• loud colors or unusual fonts, etc

```html
<!DOCTYPE html>
<html lang="en">
<head>
<meta charset="utf-8">
<title>Nexa Business Card</title>
<link href="https://fonts.googleapis.com/css2?family=Arimo:wght@400;700&display=swap" rel="stylesheet">
<style>
  :root {
    --bg: #ebebeb;
    --card: #fbfbfb;
    --ink: #2a2a2a;
    --navy: #221f63;
    --blue: #36a2d8;
    --white: #ffffff;
  }
  * { margin: 0; padding: 0; box-sizing: border-box; }
  html, body { width: 1200px; height: 1200px; overflow: hidden; }
  body {
    background: var(--bg);
    font-family: "Arimo", Arial, sans-serif;
    color: var(--ink);
    position: relative;
  }
  .card {
    position: absolute;
    left: 180px;
    width: 840px;
    height: 480px;
    background: var(--card);
    box-shadow: 0 10px 30px rgba(0,0,0,0.12);
  }
  .card--front { top: 90px; }
  .card--back { top: 630px; display: flex; align-items: center; justify-content: center; }

  .brand { display: flex; align-items: center; gap: 16px; }
  .brand__square { width: 52px; height: 52px; background: var(--blue); }
  .brand__name { font-weight: 700; font-size: 54px; color: var(--navy); letter-spacing: 2px; }
  .card--front .brand { position: absolute; left: 90px; top: 205px; }
  .card--back .brand__square { width: 64px; height: 64px; }
  .card--back .brand__name { font-size: 68px; }

  .divider {
    position: absolute; left: 400px; top: 90px;
    width: 4px; height: 300px; background: var(--blue);
  }
  .identity { position: absolute; left: 450px; top: 100px; }
  .identity__name { font-weight: 700; font-size: 44px; text-transform: uppercase; line-height: 1; }
  .identity__title { font-size: 22px; margin-top: 8px; }
  .identity__rule { width: 120px; height: 4px; background: var(--blue); margin-top: 8px; }

  .contacts { position: absolute; left: 450px; top: 232px; list-style: none; }
  .contact { display: flex; align-items: center; gap: 18px; height: 40px; margin-bottom: 8px; font-size: 24px; }
  .contact__icon {
    width: 34px; height: 34px; border-radius: 6px; background: var(--blue);
    display: flex; align-items: center; justify-content: center;
  }
  .contact__icon svg { width: 22px; height: 22px; }
</style>
</head>
<body>
  <section class="card card--front" aria-label="Business card front">
    <div class="brand">
      <span class="brand__square"></span>
      <span class="brand__name">NEXA</span>
    </div>
    <div class="divider"></div>
    <div class="identity">
      <h1 class="identity__name">Daniel Reyes</h1>
      <p class="identity__title">IT Consultant</p>
      <div class="identity__rule"></div>
    </div>
    <ul class="contacts">
      <li class="contact">
        <span class="contact__icon">
          <svg viewBox="0 0 24 24" fill="none" stroke="#fff" stroke-width="2"><rect x="3" y="6" width="18" height="12"/><path d="M3 6l9 7 9-7M3 18l7-6M21 18l-7-6"/></svg>
        </span>
        <span>daniel.reyes@nexa.ca</span>
      </li>
      <li class="contact">
        <span class="contact__icon">
          <svg viewBox="0 0 24 24" fill="#fff"><path d="M7 3l3 4-2 2c1 2.5 3.5 5 6 6l2-2 4 3-2 3c-6 0-13-7-13-13z"/></svg>
        </span>
        <span>(800) 555-0142</span>
      </li>
      <li class="contact">
        <span class="contact__icon">
          <svg viewBox="0 0 24 24" fill="none" stroke="#fff" stroke-width="2"><rect x="7" y="3" width="10" height="18" rx="2"/><path d="M11 18h2"/></svg>
        </span>
        <span>(604) 555-0187</span>
      </li>
      <li class="contact">
        <span class="contact__icon">
          <svg viewBox="0 0 24 24" fill="none" stroke="#fff" stroke-width="1.6"><circle cx="12" cy="12" r="9"/><ellipse cx="12" cy="12" rx="4" ry="9"/><path d="M3 12h18M5 7h14M5 17h14"/></svg>
        </span>
        <span>www.nexa.ca</span>
      </li>
    </ul>
  </section>

  <section class="card card--back" aria-label="Business card back">
    <div class="brand">
      <span class="brand__square"></span>
      <span class="brand__name">NEXA</span>
    </div>
  </section>
</body>
</html>
```